3 JPG Website Page Mockups need tidying / made into layered PSDs

Our website is aimed at creating a financial eduction site for females.

We have mockups of each page which are provided in jpeg.... but they need to be tidied up, layered into PSD (with descriptive layer names to allow coding from and no flattening - each object needs it's own layer) and we welcome any creative improvements suggested (although we are pretty happy with the way it's laid out at the moment as it is), without changing the feel, colour scheme or functionality of the site.

Three pages are needed:
Home page when not logged in
Home page when logged in
Topic header page

Please just upload the homepage to bid for the job... the winning designer will then have 5 days after they've been chosen to supply the psds of the other 2 pages .

I have also uploaded an image that can be used as a placeholder in the top box.
Thanks
Updates

As requested... Current font is Gill Sans MT

Thanks

Hi
Thanks for your designs.... For those of you still using the 4 circles (which I quite like), but haven't yet done so, could you see if you can move them around slightly to that the words don't get covered by the next circle?

Thanks

Reason: Designe has asked for An extension to work on new icons... would like to give them the time to see what they come up with, thanks

Industry/Entity Type

Financial

Requirements
Must have
• Maintain current feel & colour scheme of the website

```html
<!DOCTYPE html>
<html lang="en">
<head>
<meta charset="utf-8">
<title>Her Wealth Hub – Home</title>
<link href="https://fonts.googleapis.com/css2?family=Bebas+Neue&family=Cabin:wght@400;500;600&family=Arimo:wght@400;700&display=swap" rel="stylesheet">
<style>
:root{
  --teal:#1a9aa3;
  --teal-dark:#0d7a84;
  --teal-light:#3cc3cc;
  --orange:#e0441f;
  --orange-dark:#b8320f;
  --ink:#3a3a3a;
  --grey-bg:#e4e4e4;
  --grey-mid:#8a8a8a;
  --white:#ffffff;
  --sage:#a9bf94;
  --sky:#dbe8f1;
}
*{box-sizing:border-box;margin:0;padding:0}
html,body{width:1200px;height:1086px;overflow:hidden;background:#fff}
body{position:relative;font-family:"Cabin",sans-serif;color:var(--ink)}
.abs{position:absolute}

/* top navigation */
.main-nav{left:0;top:0;width:1200px;height:53px;background:linear-gradient(#22a8b1,#0e838d);border-bottom:2px solid #0a6b74}
.nav-item{top:0;height:53px;line-height:53px;color:#fff;font-size:15.5px}
.nav-home{left:26px;top:8px;width:94px;height:36px;line-height:36px;text-align:center;background:linear-gradient(#e9fbfc,#9de3e8);border-radius:4px;color:var(--teal-dark);box-shadow:0 0 6px #bff4f7}
.region{left:1096px;top:0;height:53px;display:flex;align-items:center;gap:8px;color:#fff;font-size:14px}
.region-flag{width:22px;height:14px;background:#1f3a8a;border:1px solid #fff}

/* header */
.site-header{left:0;top:55px;width:1200px;height:197px;background:var(--grey-bg)}
.brand{left:26px;top:118px;font-size:48px;color:#2a2a2a}
.search-title{left:418px;top:82px;font-family:"Bebas Neue",sans-serif;font-size:27px;color:var(--orange)}
.search-box{left:418px;top:128px;width:378px;height:46px;background:#fff;border:1px solid #c9c9c9;border-radius:23px;box-shadow:inset 0 2px 3px #ddd}
.search-box span{position:absolute;left:20px;top:13px;font-size:16px;color:#999}
.search-box svg{position:absolute;right:16px;top:10px}
.pill{top:128px;width:170px;height:46px;border-radius:23px;color:#fff;font-size:16px;line-height:46px;padding-left:20px}
.pill .chev{position:absolute;right:10px;top:11px;width:24px;height:24px;border-radius:50%;background:#fff}
.pill-adviser{left:814px;background:linear-gradient(#3ed0da,#16a3ad);color:#0d4f55}
.pill-contact{left:996px;background:linear-gradient(#f05a2c,#cc3510)}
.quick-tab{left:419px;top:202px;width:150px;height:25px;line-height:25px;text-align:center;background:var(--grey-mid);color:#fff;border-radius:2px;font-size:16px}
.quick-link{top:202px;line-height:25px;font-size:16.5px;color:#333}

/* welcome strip */
.welcome{left:0;top:252px;width:1200px;height:82px;background:#f3f3f3}
.welcome-title{left:26px;top:269px;font-size:35px;color:#333}
.member-q{left:755px;top:280px;font-family:"Bebas Neue",sans-serif;font-size:24px;color:var(--orange)}
.login{left:944px;top:263px;width:58px;height:58px;border-radius:50%;background:#2d2d2d;color:#fff;font-family:"Bebas Neue",sans-serif;font-size:21px;text-align:center;line-height:58px}
.forgot{left:1024px;top:281px;font-size:16.5px;color:var(--teal-dark)}

/* hero */
.hero{left:0;top:334px;width:1200px;height:336px;background:linear-gradient(175deg,#c9dcdf 0%,#eaf1f2 55%,#fafafa 100%)}
.hero-title{left:26px;top:352px;font-family:"Bebas Neue",sans-serif;font-size:44px;line-height:50px;color:#444;width:560px}
.join-btn{left:25px;top:514px;width:252px;height:38px;border-radius:19px;background:linear-gradient(#e8552a,#b8320f);color:#fff;font-family:"Bebas Neue",sans-serif;font-size:31px;text-align:center;line-height:40px}
.email-field{left:25px;top:577px;width:255px;height:41px;border-radius:21px;background:#fafafa;border:2px solid #d2d2d2;font-family:"Bebas Neue",sans-serif;font-size:24px;color:#888;line-height:39px;padding-left:16px}
.email-field svg{position:absolute;right:8px;top:9px}
.dots{left:25px;top:642px;display:flex;gap:17px}
.dots i{width:13px;height:13px;border-radius:50%;background:var(--teal-dark);box-shadow:inset 0 -2px 2px #064}
.dots i:first-child{background:#777}
.hero-photo{left:634px;top:350px;width:540px;height:304px;border:2px solid #fff;background:linear-gradient(120deg,#cfd8c8 0%,#e9d9c4 40%,#e07055 65%,#b9c4b0 100%)}

/* feature */
.feature{left:0;top:670px;width:1200px;height:296px;background:#efefef}
.video-card{left:24px;top:692px;width:300px;height:248px;background:#fff;border:1px solid #bbb;border-radius:4px}
.video-frame{left:34px;top:702px;width:280px;height:210px;background:linear-gradient(100deg,#3a2a22 0%,#6a4f3c 45%,#4a3a30 100%)}
.video-play{left:150px;top:782px;width:50px;height:50px;background:rgba(0,0,0,.55)}
.caption{left:62px;top:854px;width:140px;height:44px;background:rgba(110,150,110,.9);color:#fff;padding:4px 8px}
.caption b{display:block;font-size:13px;letter-spacing:1px}
.caption span{display:block;font-size:7.5px;letter-spacing:.5px;line-height:9px}
.video-bar{left:34px;top:916px;width:280px;height:14px;font-size:9px;color:#444;display:flex;align-items:center;gap:6px;padding-left:4px}
.video-bar .track{flex:1;height:3px;background:#ccc}
.topic-label{left:347px;top:704px;font-family:"Bebas Neue",sans-serif;font-size:30px;color:#3a3a3a}
.topic-head{left:347px;top:746px;font-family:"Bebas Neue",sans-serif;font-size:42px;line-height:50px;color:var(--orange)}
.learn{left:346px;top:854px;font-size:19px;color:#333}
.bubble{border-radius:50%;text-align:center;display:flex;flex-direction:column;align-items:center;justify-content:center;font-family:"Arimo",sans-serif}
.b-guide{left:738px;top:796px;width:84px;height:84px;background:#fff;border:5px solid var(--sage);font-size:11px;font-weight:700;color:#333}
.b-guide big{font-size:19px;line-height:18px}
.b-guide small{color:var(--sage);font-size:10px}
.b-poll{left:812px;top:741px;width:130px;height:130px;background:var(--sky);border:2px solid #c7d6e0;font-size:13px;font-weight:700;color:#333;justify-content:flex-start;padding-top:86px;line-height:16px}
.b-poll svg{position:absolute;left:14px;top:38px}
.b-poll em{font-style:normal;color:#7aa35f}
.b-stories{left:927px;top:697px;width:114px;height:114px;background:#fff;border:6px solid #f1ecc8;font-size:13px;font-weight:700;color:#333;line-height:20px}
.b-stories em{font-style:normal;color:#7aa35f;font-size:12px}
.b-ask{left:1019px;top:736px;width:156px;height:156px;background:var(--sage);border:3px solid #d9e3cd;color:#fff;font-size:12px;line-height:15px;padding:0 12px}
.b-ask small{font-size:10px;margin-top:8px}

/* bottom dock */
.dock{left:0;top:966px;width:1200px;height:120px;background:linear-gradient(#f4f4f4,#d3d3d3);border-top:3px solid var(--teal)}
.dock-item{top:985px;width:130px;text-align:center;font-family:"Arimo",sans-serif;font-weight:700;font-size:15px;color:#333}
.dock-icon{display:block;margin:0 auto 8px;width:58px;height:58px;border-radius:50%;background:radial-gradient(circle at 40% 30%,#6ee2ea,#0f8f99 70%);border:3px solid #fff;box-shadow:0 1px 3px #888}
.dock-icon.active{background:radial-gradient(circle at 40% 30%,#f8815c,#c7330f 70%)}
.dock-icon svg{margin-top:12px}
</style>
</head>
<body>

<nav class="abs main-nav" aria-label="Main"></nav>
<div class="abs nav-home">Home</div>
<div class="abs nav-item" style="left:157px">Polls Events</div>
<div class="abs nav-item" style="left:296px">Learning Centre</div>
<div class="abs nav-item" style="left:467px">Find an Adviser</div>
<div class="abs nav-item" style="left:628px">Ask a Qestion</div>
<div class="abs nav-item" style="left:782px">About Us</div>
<div class="abs region"><span class="region-flag"></span>AU <span style="font-size:11px">▼</span></div>

<header class="abs site-header"></header>
<div class="abs brand">Company Logo</div>
<div class="abs search-title">What are you looking for?</div>
<div class="abs search-box"><span>Search Her Wealth Hub for...</span>
  <svg width="26" height="26" viewBox="0 0 26 26"><circle cx="10" cy="10" r="7" fill="none" stroke="#1fb3bd" stroke-width="3"/><line x1="15" y1="15" x2="23" y2="23" stroke="#1fb3bd" stroke-width="4" stroke-linecap="round"/></svg>
</div>
<div class="abs pill pill-adviser">Find an Adviser<span class="chev"><svg width="24" height="24" viewBox="0 0 24 24"><path d="M7 10l5 6 5-6z" fill="#16a3ad"/></svg></span></div>
<div class="abs pill pill-contact">Contact Us<span class="chev"><svg width="24" height="24" viewBox="0 0 24 24"><path d="M7 10l5 6 5-6z" fill="#cc3510"/></svg></span></div>
<div class="abs quick-tab">Popular Searches</div>
<div class="abs quick-link" style="left:596px">Explore the Learning Centre</div>
<div class="abs quick-link" style="left:839px">Ask a Question</div>

<section class="abs welcome"></section>
<h1 class="abs welcome-title" style="font-weight:400">Welcome to the new financial woman site</h1>
<div class="abs member-q">All ready a member?</div>
<div class="abs login">Login</div>
<div class="abs forgot">Forgotten Password</div>

<section class="abs hero"></section>
<h2 class="abs hero-title" style="font-weight:400">We’re building Australia a biggest community dedicated to the financial empowerment of woman</h2>
<div class="abs join-btn">Join now for free</div>
<div class="abs email-field">Insert email address
  <svg width="22" height="22" viewBox="0 0 22 22"><circle cx="11" cy="11" r="9" fill="none" stroke="#999" stroke-width="1.5"/><path d="M9 7l5 4-5 4z" fill="#888"/></svg>
</div>
<div class="abs dots"><i></i><i></i><i></i><i></i><i></i></div>
<div class="abs hero-photo" role="img" aria-label="Photo of a smiling woman in a coral cardigan seated at a table in a sunny room"></div>

<section class="abs feature"></section>
<div class="abs video-card"></div>
<div class="abs video-frame" role="img" aria-label="Video still of a woman speaking in front of a bookshelf"></div>
<div class="abs video-play"><svg width="50" height="50" viewBox="0 0 50 50"><path d="M19 14l16 11-16 11z" fill="#fff"/></svg></div>
<div class="abs caption"><b>MARA ELLISON</b><span>FOUNDER, CHAIRMAN &amp; CEO<br>HEARTH &amp; CO.</span></div>
<div class="abs video-bar">▶ ■ <span>00:00</span><span class="track"></span><span>00:00</span></div>
<div class="abs topic-label">July topic: Preparing for retirement</div>
<div class="abs topic-head">Tomorrow can belong to those<br>who prepare today</div>
<div class="abs learn">Learn More ›</div>

<div class="abs bubble b-poll">
  <svg width="100" height="40" viewBox="0 0 100 40">
    <g fill="#8fc06a">
      <rect x="0" y="32" width="6" height="6"/><rect x="9" y="30" width="6" height="8"/><rect x="18" y="28" width="6" height="10"/><rect x="27" y="25" width="6" height="13"/><rect x="36" y="22" width="6" height="16"/><rect x="45" y="18" width="6" height="20"/><rect x="54" y="14" width="6" height="24"/><rect x="63" y="10" width="6" height="28"/><rect x="72" y="6" width="6" height="32"/><rect x="81" y="3" width="6" height="35"/><rect x="90" y="3" width="6" height="35"/>
    </g>
  </svg>
  <span>Take Our Poll</span><em>Vote &gt;</em>
</div>
<div class="abs bubble b-guide"><span>5 Minute</span><big>Guide</big><small>PDF &gt;</small></div>
<div class="abs bubble b-stories"><span>Real Women<br>Real Stories</span><em>See Video</em></div>
<div class="abs bubble b-ask"><span>Have questions<br>about Life Stages &amp;<br>Planning? Ask a<br>question or see what<br>others have asked...</span><small>More &gt;</small></div>

<footer class="abs dock"></footer>
<div class="abs dock-item" style="left:36px"><span class="dock-icon active"><svg width="30" height="30" viewBox="0 0 30 30" fill="#fff"><circle cx="15" cy="9" r="5"/><path d="M6 27c0-7 4-11 9-11s9 4 9 11z"/></svg></span>Welcome</div>
<div class="abs dock-item" style="left:179px"><span class="dock-icon"><svg width="30" height="30" viewBox="0 0 30 30" fill="none" stroke="#fff" stroke-width="2"><rect x="4" y="6" width="22" height="20"/><line x1="4" y1="11" x2="26" y2="11"/><line x1="11" y1="11" x2="11" y2="26"/><line x1="18" y1="11" x2="18" y2="26"/><line x1="4" y1="18" x2="26" y2="18"/></svg></span>Events</div>
<div class="abs dock-item" style="left:318px"><span class="dock-icon"><svg width="30" height="30" viewBox="0 0 30 30" fill="none" stroke="#fff" stroke-width="2"><rect x="4" y="9" width="22" height="16" rx="2"/><path d="M11 4l4 5 4-5"/></svg></span>Webcasts</div>
<div class="abs dock-item" style="left:465px"><span class="dock-icon"><svg width="30" height="30" viewBox="0 0 30 30" fill="#fff"><path d="M15 4L3 15h4v11h6v-7h4v7h6V15h4z"/></svg></span>My Family</div>
<div class="abs dock-item" style="left:606px"><span class="dock-icon"><svg width="30" height="30" viewBox="0 0 30 30" fill="none" stroke="#fff" stroke-width="2"><path d="M4 4v22h22"/><path d="M7 21l6-7 5 4 7-9"/></svg></span>My Investments</div>
<div class="abs dock-item" style="left:752px"><span class="dock-icon"><svg width="30" height="30" viewBox="0 0 30 30" fill="none" stroke="#fff" stroke-width="2"><circle cx="15" cy="16" r="10"/><path d="M15 10v6l4 3"/><path d="M5 6l4-3M25 6l-4-3"/></svg></span>My Retirement</div>
<div class="abs dock-item" style="left:895px"><span class="dock-icon"><svg width="30" height="30" viewBox="0 0 30 30" fill="none" stroke="#fff" stroke-width="2"><path d="M8 26V12l4-6 2 1-2 6h10l-1 13z"/></svg></span>My Estate</div>
<div class="abs dock-item" style="left:1037px"><span class="dock-icon"><svg width="30" height="30" viewBox="0 0 30 30" fill="none" stroke="#fff" stroke-width="2"><path d="M9 4h12c0 8-2 12-6 12s-6-4-6-12z"/><path d="M15 16v9M10 26h10"/></svg></span>My Lifestyle</div>

</body>
</html>
```